VOLTIQ4 Website design (Need help to re-design our website)

We need someone to help us re-design our website and launch it. All contents for the website are ready. (Website: https://www.voltiq4.com.au/)

-Rearrange categories:
1. Heat Pumps (Link to KALVO site: https://kalvo.com.au/)
2. Solar (Under the Solar category; remove solar panels, solar inverters, and solar batteries)
3. LED
4. Capability Statement
5. Service and Support
6. Contact us

Home page - redesign but the free quote will stay.

NOTE:
-Try using professional fonts (Example: Helvetica, etc.)
-Try to play with colours related to sustainability, eco-friendliness, solar, energy, and energy efficiency.
-The website's Footer should be readable and use light colour.

Target Market(s)

Residentials & commercial buildings

Industry/Entity Type

SOLAR ENERGY PROVIDER

Coding

Coded - Design and coding required

Colors

Designer to choose colors to be used in the design.

Requirements
Nice to have
• Effects/transition on the words/copy/images.

```html
<!DOCTYPE html>
<html lang="en">
<head>
<meta charset="utf-8">
<title>VOLTIQ4 — Energy Efficiency</title>
<link href="https://fonts.googleapis.com/css2?family=Roboto:wght@400;500;700;900&display=swap" rel="stylesheet">
<style>
:root{
  --navy:#112064;
  --navy-dark:#0b1650;
  --green:#4eae2f;
  --green-bright:#6cc83a;
  --green-pale:#eef8e3;
  --lime:#a8ea63;
  --blue:#1f6fd1;
  --ink:#1d1d1d;
  --muted:#555;
  --white:#fff;
}
*{box-sizing:border-box;margin:0;padding:0}
html,body{width:1200px;height:5072px;overflow:hidden}
body{position:relative;font-family:"Roboto",Helvetica,Arial,sans-serif;color:var(--ink);background:var(--white)}
.abs{position:absolute}
.brand{font-weight:900;color:var(--navy);font-size:28px;letter-spacing:.5px;display:flex;align-items:center;gap:8px}
.brand .dot{width:16px;height:16px;border-radius:50%;background:var(--green)}
.btn{display:inline-block;background:var(--green);color:#fff;font-weight:700;font-size:13px;padding:11px 18px;border-radius:3px}
.eyebrow{color:var(--green);font-size:16px;letter-spacing:.5px}
.hl-green{color:var(--green)}
.hl-blue{color:var(--blue)}

/* hero */
.hero-photo{left:0;top:0;width:1200px;height:650px;background:linear-gradient(180deg,#2d3a2a 0%,#4f6b3c 45%,#6c8550 70%,#2f4a2e 100%)}
.topbar{left:0;top:0;width:1200px;height:50px;color:#fff;font-size:15px}
.topbar span{position:absolute;top:14px}
.social{position:absolute;top:14px;width:22px;height:22px;border-radius:50%;background:#fff}
.nav{left:106px;top:50px;width:986px;height:76px;background:#fff;border-radius:3px;box-shadow:0 4px 12px rgba(0,0,0,.15)}
.nav .brand{position:absolute;left:22px;top:22px}
.nav ul{position:absolute;right:28px;top:30px;list-style:none;display:flex;gap:26px;font-size:16px;color:#222}
.hero-copy{left:106px;top:220px;width:520px;color:#fff}
.hero-copy h1{font-size:44px;line-height:1.25;font-weight:700}
.hero-copy h1 span{color:var(--green-bright)}
.hero-copy p{margin-top:24px;font-size:15.5px;line-height:1.7}
.hero-copy .btn{margin-top:26px}
.quote{left:750px;top:165px;width:340px;height:370px;background:linear-gradient(160deg,#5bbd34,#3f9a26);border-radius:6px;padding:0 38px}
.quote .ico{position:absolute;left:152px;top:12px;width:36px;height:36px;border-radius:50%;background:#7ad14c}
.quote h3{margin-top:60px;text-align:center;color:#fff;font-size:20px;font-weight:700}
.field{height:34px;background:#fff;border-radius:3px;margin-top:10px;font-size:13px;padding:10px 12px;color:#333}
.field:first-of-type{margin-top:18px}
.submit{height:36px;background:#0a1a2f;color:#fff;text-align:center;font-size:14px;font-weight:700;padding-top:10px;border-radius:3px;margin-top:12px}

/* about */
.about-photo{left:136px;top:790px;width:410px;height:320px;background:linear-gradient(135deg,#dfe3e6,#b9c0c5 60%,#8a98a5);border:3px solid var(--green);clip-path:polygon(0 0,88% 0,100% 13%,100% 100%,12% 100%,0 87%)}
.years{left:106px;top:766px;width:110px;height:110px;border-radius:50%;background:var(--blue);border:4px solid #fff;color:#fff;text-align:center}
.years b{display:block;font-size:36px;margin-top:18px}
.years small{font-size:12px;font-weight:700;line-height:1.2;display:block}
.about-copy{left:612px;top:750px;width:490px;color:#fff}
.about-copy h2{font-size:38px;font-weight:700;margin-top:8px}
.about-copy p{font-size:15.5px;line-height:1.9;margin-top:14px}
.about-copy .lead{font-weight:700;font-size:18px;margin-top:10px}

/* services */
.section-title{text-align:center;font-size:38px;font-weight:700;line-height:1.25}
.svc-band{left:0;top:1645px;width:1200px;height:700px;background:var(--green-pale)}
.card{top:1481px;width:310px;height:348px;background:#fff;border:3px solid #d8d8d8}
.card .pic{position:absolute;left:16px;top:12px;width:272px;height:148px}
.card h4{position:absolute;left:24px;top:178px;color:var(--blue);font-size:23px;font-weight:700}
.card p{position:absolute;left:24px;top:215px;width:255px;font-size:16px;line-height:1.6;color:#444}
.card .more{position:absolute;right:0;bottom:0;width:160px;height:54px;background:var(--green);color:#fff;font-weight:700;font-size:14px;padding:18px 0 0 14px;clip-path:polygon(0 0,75% 0,100% 100%,0 100%)}
.strip{background:#fff;box-shadow:0 14px 24px rgba(0,0,0,.12)}
.badge{position:absolute;top:40px;height:40px;border-radius:6px}
.arrow{position:absolute;width:32px;height:32px;border-radius:50%;display:flex;align-items:center;justify-content:center}

/* projects */
.proj{top:2512px;height:346px;border-radius:4px;overflow:hidden}
.proj b{position:absolute;left:28px;bottom:32px;color:#fff;font-size:22px}
.proj i{position:absolute;right:20px;bottom:28px;width:32px;height:32px;border-radius:50%;border:2px solid var(--green-bright)}
.ghost{left:78px;top:2900px;font-size:110px;font-weight:900;letter-spacing:28px;color:rgba(255,255,255,.06)}

/* reviews */
.reviews-bg{left:0;top:2985px;width:1200px;height:660px;background-color:var(--lime);background-image:linear-gradient(rgba(255,255,255,.18) 1px,transparent 1px),linear-gradient(90deg,rgba(255,255,255,.18) 1px,transparent 1px);background-size:48px 48px}
.review{top:3220px;width:486px;height:325px;background:#fff;text-align:center;padding:80px 40px 0}
.review h5{color:var(--navy);font-size:22px;font-weight:700}
.stars{color:#f5b400;font-size:20px;letter-spacing:2px}
.review p{font-size:16px;line-height:1.5;color:#555;margin-top:12px}
.review .src{margin-top:10px;font-weight:700;color:var(--blue);font-size:18px}
.avatar{top:3170px;width:100px;height:100px;border-radius:50%;border:3px solid var(--navy);background:radial-gradient(circle at 50% 40%,#cfd6dc,#8e9aa4)}

/* clients */
.client{position:absolute;top:48px;font-weight:700;font-size:21px;color:var(--navy)}

/* newsletter */
.news{left:0;top:4160px;width:1200px;text-align:center;color:#fff}
.news h2{font-size:38px;font-weight:700;margin-top:4px}
.news p{font-size:19px;margin-top:18px}
.subscribe{left:366px;top:4340px;width:468px;height:46px;background:#fff;border-radius:3px}
.subscribe span{position:absolute;left:20px;top:15px;font-size:14px;color:#333}
.subscribe b{position:absolute;right:6px;top:7px;width:124px;height:32px;background:var(--green);color:#fff;font-size:14px;text-align:center;padding-top:8px;border-radius:2px}
.contact-bar{left:106px;top:4497px;width:986px;height:70px;background:linear-gradient(90deg,#5cbf34,#4aa52c);border-radius:3px;color:#fff}
.cb{position:absolute;top:14px;display:flex;gap:18px;align-items:center}
.cb .ring{width:38px;height:38px;border-radius:50%;border:2px solid rgba(255,255,255,.7)}
.cb small{display:block;font-size:13px}
.cb strong{font-size:17px}

/* footer */
.foot-col{top:4648px;font-size:15px;color:#444;line-height:1.75}
.foot-col h6{color:var(--blue);font-size:18px;font-weight:700;margin-bottom:12px}
.loc{display:flex;gap:14px;border-bottom:2px solid var(--green);padding:6px 0 4px;width:204px;line-height:1.45}
.loc i{width:12px;height:12px;border-radius:50% 50% 50% 0;background:var(--green);transform:rotate(-45deg);margin-top:4px;flex:none}
.fsoc{position:absolute;top:5038px;width:18px;height:18px;border-radius:3px;background:var(--navy)}
</style>
</head>
<body>

<!-- HERO -->
<div class="abs hero-photo" role="img" aria-label="Aerial view of a large solar farm at sunset"></div>
<div class="abs topbar">
  <span style="left:108px">✉ enquiries@voltiq4.com.au</span>
  <span style="left:388px">☎ 1300 555 018</span>
  <i class="social" style="left:1004px;background:var(--green)"></i>
  <i class="social" style="left:1034px"></i>
  <i class="social" style="left:1064px"></i>
</div>
<nav class="abs nav">
  <div class="brand"><i class="dot"></i>VOLTIQ4</div>
  <ul><li>Heat Pumps</li><li>Solar</li><li>LED</li><li>Capability Statement</li><li>Service and Support</li><li>Contact us</li></ul>
</nav>
<div class="abs hero-copy">
  <h1>Our Aims To Improve Your Energy <span>Efficiency</span></h1>
  <p>Save on electricity costs by switching to solar!<br>Did you know that you could install a solar system for a lower price than your current electricity costs!</p>
  <span class="btn">Get In Touch Now</span>
</div>
<form class="abs quote">
  <i class="ico"></i>
  <h3>WANT A FREE QUOTE?</h3>
  <div class="field">Name</div>
  <div class="field">Email</div>
  <div class="field">Phone Number</div>
  <div class="field">Address</div>
  <div class="field">I am interested in <span style="float:right">⌄</span></div>
  <div class="submit">Submit Now</div>
</form>

<svg class="abs" style="left:0;top:470px" width="1200" height="190" viewBox="0 0 1200 190">
  <path d="M0,30 C250,190 700,170 1200,70 L1200,190 L0,190Z" fill="#112064"/>
  <path d="M0,30 C250,190 700,170 1200,70" fill="none" stroke="#4eae2f" stroke-width="9"/>
</svg>

<!-- ABOUT -->
<div class="abs" style="left:0;top:650px;width:1200px;height:660px;background:var(--navy)"></div>
<div class="abs about-photo" role="img" aria-label="Professional holding a small wind turbine model and a solar panel"></div>
<div class="abs years"><b>25</b><small>YEARS<br>Experienced</small></div>
<div class="abs about-copy">
  <div class="eyebrow">ABOUT US</div>
  <h2>What Is <span class="hl-green">VOLTIQ4 ?</span></h2>
  <p>Power bills have risen dramatically in Australia over the past decade, making energy bills amongst the highest utility expense for businesses and households alike.</p>
  <p class="lead">That's where we come in!</p>
  <p style="margin-top:6px">We are a completely Australian Owned and Operated company that specialise in adapting the latest technologies to improve your energy efficiency and reduce costs.</p>
  <span class="btn" style="margin-top:30px;padding:11px 40px">Read More</span>
</div>
<svg class="abs" style="left:0;top:1210px" width="1200" height="110" viewBox="0 0 1200 110">
  <path d="M0,100 C300,10 900,10 1200,100 L1200,110 L0,110Z" fill="#fff"/>
</svg>

<!-- SERVICES -->
<div class="abs svc-band"></div>
<div class="abs eyebrow" style="left:0;top:1320px;width:1200px;text-align:center">SERVICES</div>
<h2 class="abs section-title" style="left:0;top:1350px;width:1200px">When You Choose VOLTIQ4, You<br><span class="hl-blue">Are In Safe Hands</span></h2>

<div class="abs card" style="left:106px">
  <div class="pic" role="img" aria-label="Rows of solar panels in a green field" style="background:linear-gradient(180deg,#7d9a6a,#3d4f6a 55%,#5f7a46)"></div>
  <h4>SOLAR ENERGY</h4><p>Solar is great for the environment and great for your pocket!</p>
  <span class="more">Read More »</span>
</div>
<div class="abs card" style="left:446px">
  <div class="pic" role="img" aria-label="Office interior lit by LED ceiling lighting" style="background:linear-gradient(180deg,#0f3940,#1d6d6e 40%,#2b2b35)"></div>
  <h4>LED</h4><p>Our company works under the Regional Power Saver (RPS) program...</p>
  <span class="more">Read More »</span>
</div>
<div class="abs card" style="left:786px">
  <div class="pic" role="img" aria-label="Heat pump unit beside a home with a phone app" style="background:linear-gradient(135deg,#e8e2da,#b08c6e 55%,#8a6a52)"></div>
  <h4>HEAT PUMP</h4><p>Heat pump water heaters use electricity to take out the surrounding air ..</p>
  <span class="more">Read More »</span>
</div>

<h2 class="abs" style="left:0;top:1938px;width:1200px;text-align:center;font-size:36px;font-weight:500">Accreditations &amp; <span class="hl-blue">Partners</span></h2>
<div class="abs strip" style="left:104px;top:2017px;width:988px;height:118px">
  <i class="badge" style="left:58px;width:172px;background:#d7ecd2"></i>
  <i class="badge" style="left:316px;top:22px;width:48px;height:76px;background:#1b2a6b"></i>
  <i class="badge" style="left:444px;width:140px;background:#f1d9d6"></i>
  <i class="badge" style="left:680px;width:126px;background:#3a3a3a"></i>
  <i class="badge" style="left:880px;top:30px;width:52px;height:56px;border-radius:50%;background:#e6f0b3"></i>
</div>
<div class="arrow" style="left:92px;top:2060px;background:#888;color:#fff">‹</div>
<div class="arrow" style="left:1074px;top:2060px;background:var(--green);color:#fff">›</div>

<!-- PROJECTS -->
<svg class="abs" style="left:0;top:2240px" width="1200" height="170" viewBox="0 0 1200 170">
  <path d="M0,160 C300,40 700,10 1200,20 L1200,170 L0,170Z" fill="#112064"/>
  <path d="M0,160 C300,40 700,10 1200,20" fill="none" stroke="#4eae2f" stroke-width="9"/>
</svg>
<div class="abs" style="left:0;top:2405px;width:1200px;height:580px;background:var(--navy)"></div>
<div class="abs ghost">PROJECTS</div>
<div class="abs eyebrow" style="left:106px;top:2414px;color:var(--green-bright)">WORKS</div>
<h2 class="abs" style="left:106px;top:2438px;color:#fff;font-size:38px;font-weight:700">Our <span style="color:var(--green-bright)">Projects</span></h2>
<div class="abs proj" style="left:106px;width:566px" role="img" aria-label="Aerial view of a floating solar array on a dam"><div style="position:absolute;inset:0;background:linear-gradient(180deg,#c6b4a0,#4e5a6a 40%,#a08a74 80%,#6e5c4d)"></div><b>502 kW - Dam 5</b><i></i></div>
<div class="abs proj" style="left:698px;width:234px" role="img" aria-label="Long rows of solar panels beside a river"><div style="position:absolute;inset:0;background:linear-gradient(180deg,#9bb3c8,#4a5b70 45%,#7c6d55)"></div><b style="left:20px">502 kW</b><i></i></div>
<div class="abs proj" style="left:953px;width:247px" role="img" aria-label="Ground-mounted solar installation"><div style="position:absolute;inset:0;background:linear-gradient(90deg,#2e3f6e,#112064)"></div><b style="left:20px;color:rgba(255,255,255,.45)">250 KW</b></div>
<div class="arrow" style="left:1090px;top:2640px;background:#888;color:#fff">‹</div>
<div class="arrow" style="left:1090px;top:2694px;background:var(--green);color:#fff">›</div>

<!-- REVIEWS -->
<div class="abs reviews-bg"></div>
<h2 class="abs" style="left:0;top:3096px;width:1200px;text-align:center;color:var(--blue);font-size:38px;font-weight:700">Trustline Review</h2>
<div class="abs review" style="left:104px">
  <h5>MARA LINDQVIST</h5><div class="stars">★★★★★</div>
  <p>“ I had my solar system installed almost a year ago now and I'm super happy with it. The crew that came to do the installation were efficient courteous and knowledgeable and no question was left unanswered. Thank you VOLTIQ4 ”</p>
  <div class="src">Trustline</div>
</div>
<div class="abs review" style="left:608px">
  <h5>DEV RAMASWAMY</h5><div class="stars">★★★★★</div>
  <p>“ Happy with everything. I got a very good product with a very reasonable price. Also, the help me a lot through all the process, especially on the rebate application process. Very professional and knowledgeable. ”</p>
  <div class="src">Trustline</div>
</div>
<div class="abs avatar" style="left:297px" role="img" aria-label="Customer portrait"></div>
<div class="abs avatar" style="left:801px" role="img" aria-label="Customer portrait"></div>
<div class="arrow" style="left:88px;top:3366px;width:42px;height:42px;background:#c9c9c9;color:#333">‹</div>
<div class="arrow" style="left:1072px;top:3366px;width:42px;height:42px;background:#1d1d1d;color:#fff">›</div>

<!-- CLIENTS -->
<h2 class="abs" style="left:0;top:3740px;width:1200px;text-align:center;font-size:38px;font-weight:700">Our <span class="hl-blue">Clients</span></h2>
<div class="abs strip" style="left:104px;top:3822px;width:986px;height:122px">
  <span class="client" style="left:44px">Hillcrest Fencing</span>
  <span class="client" style="left:294px">Corvel Limited</span>
  <span class="client" style="left:536px">Brightguard Safety</span>
  <span class="client" style="left:784px">Northvale Steel</span>
</div>
<div class="arrow" style="left:92px;top:3872px;background:#888;color:#fff">‹</div>
<div class="arrow" style="left:1074px;top:3872px;background:var(--green);color:#fff">›</div>

<!-- NEWSLETTER -->
<svg class="abs" style="left:0;top:4070px" width="1200" height="180" viewBox="0 0 1200 180">
  <path d="M0,150 C350,40 800,20 1200,30 L1200,180 L0,180Z" fill="#112064"/>
  <path d="M0,150 C350,40 800,20 1200,30" fill="none" stroke="#4eae2f" stroke-width="9"/>
</svg>
<div class="abs" style="left:0;top:4240px;width:1200px;height:362px;background:var(--navy)"></div>
<div class="abs news">
  <div class="eyebrow">NEWSLETTER</div>
  <h2>Sign Up for the Latest <span class="hl-green">Offers</span></h2>
  <p>Get all the latest information on Special Discounts, Products and Offers.</p>
</div>
<div class="abs subscribe"><span>Enter Your Mail ID</span><b>Subscribe</b></div>
<div class="abs contact-bar">
  <div class="cb" style="left:26px"><i class="ring"></i><div><small>call our support team</small><strong>1300 555 018</strong></div></div>
  <div class="cb" style="left:346px"><i class="ring"></i><div><small>send us an email</small><strong>enquiries@voltiq4.com.au</strong></div></div>
  <div class="cb" style="left:670px"><i class="ring"></i><div><small>Business hours:</small><strong>Mon - Sun : 9AM - 5PM</strong></div></div>
</div>

<!-- FOOTER -->
<div class="abs brand" style="left:106px;top:4636px;font-size:26px"><i class="dot"></i>VOLTIQ4</div>
<p class="abs" style="left:106px;top:4704px;width:270px;font-size:15px;line-height:1.6;color:#444">We are a completely Australian Owned and Operated company with in-house solar technicians and engineers, designing the best solar system for your needs.</p>
<div class="abs foot-col" style="left:424px"><h6>OUR OFFICES</h6>Heat Pumps<br>Solar<br>LED<br>Capability Statement<br>Service and Support<br>Contact us</div>
<div class="abs foot-col" style="left:630px;line-height:1.4"><h6>OUR LOCATIONS</h6>
  <div class="loc"><i></i>24 Calder Street<br>Kensington VIC 3031</div>
  <div class="loc"><i></i>6A/41 Keller Drive<br>Nerang QLD 4211</div>
  <div class="loc"><i></i>9 Foundry Court Irymple<br>VIC 3498</div>
  <div class="loc"><i></i>118/52 Harlow St, Perth<br>WA 6000</div>
  <div class="loc" style="border:0"><i></i>5/71 Bramble Street<br>Hobart TAS 7000</div>
</div>
<div class="abs foot-col" style="left:888px"><h6>SERVICE &amp; SUPPORT</h6>Solar Panel Cleaning<br>Inverter Repairs &amp; Warranty<br>Solar Package Repair</div>
<div class="abs" style="left:106px;top:5004px;width:984px;height:1px;background:#bbb"></div>
<i class="fsoc" style="left:106px"></i><i class="fsoc" style="left:128px;border-radius:50%;background:var(--green)"></i><i class="fsoc" style="left:158px"></i><i class="fsoc" style="left:200px"></i>
<div class="abs" style="left:700px;top:5038px;width:390px;text-align:right;font-size:14px;color:#444">© Copyright 2024 <b style="color:var(--blue)">VOLTIQ4</b> All Rights Reserved</div>

</body>
</html>
```